ZEPRILO.COM is a premium domain sales company. Our competitors are companies like vastplots.example, getparcels.example, peerwords.example. Our current site is at www.zeprilos.example.

We want to have the ability to search for domains, to highlight special offers and have some testimonials on the index page.

The logo for the site is attached.

Please be sure that the order form fits on the screen without scrolling the page. I want the entire form, including the submit button to fit without any page scrolling.

Delivered product - INDEX PAGE, ORDER FORM AND CONTENT PAGE PSDs.

Target Market(s)

Small to Medium business professionals

Industry/Entity Type

It Company

Requirements
Must have
• 1. List of domains for sale
2. Simple search box with button to run the search
3. link for advanced search
4. testimonial area. Note - this can be a small box where a different testimonial is displayed on each page load.
Nice to have
• Would like the site to have some white space. Don't want a heavily packed website. Give it an "airy" feel.

```html
<!DOCTYPE html>
<html lang="en">
<head>
<meta charset="utf-8">
<title>ZEPRILO.COM – Premium domains</title>
<link rel="stylesheet" href="https://fonts.googleapis.com/css2?family=Zilla+Slab:ital,wght@0,300;0,400;0,500;1,300;1,400&family=Lato:wght@400;700;900&display=swap">
<style>
:root{
  --blue:#1b5aa2;
  --blue-dark:#0e4b8f;
  --green:#16703f;
  --green-btn:#0f6b3a;
  --red:#d6202a;
  --ink:#333;
  --muted:#666;
  --line:#dcdcdc;
  --band:#e5ecf3;
  --white:#fff;
  --grey-btn:#d4d4d4;
  --slider:#cfe3dc;
}
*{box-sizing:border-box;margin:0;padding:0}
html,body{width:1200px;height:3000px;overflow:hidden}
body{position:relative;background:var(--white);font-family:"Zilla Slab",Georgia,serif;color:var(--ink)}
.abs{position:absolute}

/* header */
.site-header{position:absolute;left:0;top:0;width:1200px;height:76px;background:var(--white);border-bottom:1px solid var(--line)}
.brand{position:absolute;left:88px;top:14px;display:flex;align-items:center;gap:10px}
.brand-mark{width:22px;height:22px;border-radius:50%;background:var(--green)}
.brand-name{font-family:"Lato",Arial,sans-serif;font-weight:900;font-size:34px;color:var(--blue);letter-spacing:-0.5px}
.main-nav{position:absolute;left:364px;top:0;height:76px;display:flex}
.main-nav a{display:flex;align-items:center;justify-content:center;height:76px;border-left:1px solid var(--line);font-size:25px;color:var(--ink);text-decoration:none}
.main-nav a.active{color:var(--blue);border-bottom:5px solid var(--blue);padding-top:5px}
.main-nav a:last-child{border-right:1px solid var(--line)}

/* hero */
.hero{position:absolute;left:0;top:76px;width:1200px;height:500px;background:linear-gradient(90deg,#7b6f63 0%,#a39a8c 35%,#c9c3b8 55%,#8b8071 75%,#6d6356 100%)}
.hero-title{position:absolute;left:88px;top:118px;font-size:58px;font-weight:300;color:var(--white)}
.hero-title em{font-style:italic}
.hero-search{position:absolute;left:88px;top:222px;display:flex}
.hero-search .field{width:382px;height:68px;background:var(--white);font-size:28px;font-style:italic;font-weight:300;color:#999;padding:16px 18px}
.hero-search .btn{width:168px;height:68px;background:var(--blue);color:var(--white);font-size:30px;display:flex;align-items:center;justify-content:center}
.hero-link{position:absolute;left:106px;top:300px;font-size:18px;font-style:italic;color:var(--white);text-decoration:underline}

/* offers */
.offers{position:absolute;left:0;top:576px;width:1200px;height:552px;background:var(--band)}
.section-title{font-size:58px;font-weight:300;color:var(--blue)}
.section-title em{font-style:italic}
.offers .section-title{position:absolute;left:88px;top:56px}
.offers-copy{position:absolute;left:88px;top:140px;width:414px;font-family:"Lato",Arial,sans-serif;font-size:12.5px;line-height:19px;color:#444}
.offers-copy p{margin-bottom:14px}
.offers-copy .more{color:var(--blue);font-weight:700}
.btn-blue{background:var(--blue);color:var(--white);display:flex;align-items:center;justify-content:center}
.offers .btn-blue{position:absolute;left:88px;top:424px;width:228px;height:70px;font-size:30px}

.domain-table{border:1px solid var(--line);background:var(--white);box-shadow:0 1px 3px rgba(0,0,0,.1)}
.domain-row{display:flex;height:76px;border-top:1px solid var(--line)}
.domain-row:first-child{border-top:0}
.domain-name{flex:1;display:flex;align-items:center;padding-left:20px;font-size:30px;color:var(--ink)}
.domain-price{display:flex;align-items:center;justify-content:center;border-left:1px solid var(--line);font-family:"Lato",Arial,sans-serif;font-weight:700;font-size:30px;color:var(--green)}
.domain-go{width:68px;display:flex;align-items:center;justify-content:center;border-left:1px solid var(--line)}
.go-btn{width:52px;height:52px;background:var(--green-btn);display:flex;align-items:center;justify-content:center}

.offer-table{position:absolute;left:512px;top:114px;width:600px}
.offer-head{height:76px;display:flex;align-items:center;padding-left:20px;font-size:30px;color:var(--blue);border-bottom:1px solid var(--line)}
.offer-head em{color:var(--red)}
.offer-table .domain-price{width:126px}
.offer-table .domain-go{width:76px}

/* browse */
.browse{position:absolute;left:0;top:1128px;width:1200px;height:1270px}
.browse .section-title{position:absolute;left:88px;top:54px}
.browse-table{position:absolute;left:88px;top:166px;width:600px}
.browse-table .domain-price{width:136px}

.pager{position:absolute;left:88px;top:1110px;width:592px;height:54px;display:flex;align-items:center;font-size:20px;color:#555}
.pager .nav-btn{width:116px;height:54px;background:var(--grey-btn);color:var(--white);display:flex;align-items:center;justify-content:center;font-size:19px;font-style:italic;gap:8px}
.pager .prev{background:#ebebeb}
.pager .pages{flex:1;display:flex;justify-content:space-around;padding:0 20px}
.pager .current{color:var(--green);font-weight:500;text-decoration:underline}

.adv{position:absolute;left:748px;top:190px;width:364px}
.adv-title{font-size:30px;color:var(--blue)}
.adv-title em{font-style:italic}
.adv-field{margin-top:22px;height:60px;border:2px solid var(--blue);font-size:24px;font-style:italic;font-weight:300;color:#999;padding:14px 18px}
.checks{margin-top:28px;display:grid;grid-template-columns:198px 166px;row-gap:22px}
.check{display:flex;align-items:center;gap:16px;font-size:23px;font-style:italic;color:#444}
.box{width:34px;height:34px;border:2px solid #333;position:relative}
.range{margin-top:30px}
.range-head{display:flex;justify-content:space-between;font-size:30px;color:var(--blue)}
.range-head em{font-style:italic;color:var(--green)}
.slider{position:relative;margin-top:14px;height:26px;border:2px solid var(--blue);background:var(--white)}
.slider .fill{position:absolute;top:0;bottom:0;background:var(--slider)}
.slider .knob{position:absolute;top:-4px;width:32px;height:30px;background:var(--green-btn);border-radius:3px;display:flex;align-items:center;justify-content:center}
.adv .btn-blue{margin:34px 0 0 auto;width:144px;height:56px;font-size:22px}

/* testimonial */
.story{position:absolute;left:0;top:2398px;width:1200px;height:552px;background:linear-gradient(90deg,#4c4240 0%,#7a6b63 25%,#a59488 45%,#c7b9b0 70%,#b3a49a 100%)}
.story-card{position:absolute;left:512px;top:66px;width:600px;height:442px;background:var(--white);padding:22px 28px;box-shadow:0 1px 4px rgba(0,0,0,.15)}
.story-card h2{font-size:56px;font-weight:300;line-height:56px;color:var(--blue)}
.story-card h2 em{font-style:italic}
.story-card .copy{margin-top:28px;font-family:"Lato",Arial,sans-serif;font-size:12.5px;line-height:19px;color:#444}
.story-card .copy p{margin-bottom:12px}
.story-card .who{margin-top:14px;font-size:30px;color:var(--blue)}
.story-card .trade{font-size:19px;color:var(--blue);margin-top:4px}
.story-card .site{font-size:19px;font-style:italic;color:var(--blue);text-decoration:underline}

/* footer */
.site-footer{position:absolute;left:0;top:2950px;width:1200px;height:50px;display:flex;align-items:center;justify-content:space-between;padding:0 88px;font-size:14px;color:#555}
.site-footer nav{display:flex;gap:10px}
</style>
</head>
<body>

<header class="site-header">
  <div class="brand"><span class="brand-mark"></span><span class="brand-name">ZEPRILO</span></div>
  <nav class="main-nav">
    <a class="active" style="width:162px">Domains</a>
    <a style="width:114px">FAQs</a>
    <a style="width:152px">About us</a>
    <a style="width:136px">Contact</a>
    <a style="width:108px">Login</a>
    <a style="width:74px" aria-label="Basket">
      <svg width="28" height="26" viewBox="0 0 28 26"><path d="M1 3h5l4 14h13l3-10H8" fill="none" stroke="#333" stroke-width="3"/><circle cx="11" cy="22" r="2.5" fill="#333"/><circle cx="22" cy="22" r="2.5" fill="#333"/></svg>
    </a>
  </nav>
</header>

<section class="hero" role="img" aria-label="Photo of a business man in a suit standing in a warehouse aisle">
  <h1 class="hero-title">It all starts with the <em>name.</em></h1>
  <div class="hero-search"><div class="field">Find your name today...</div><div class="btn">Search</div></div>
  <a class="hero-link">Or try our advanced search.</a>
</section>

<section class="offers">
  <h2 class="section-title">Special <em>offers.</em></h2>
  <div class="offers-copy">
    <p>Lorem ipsum dolor sit amet, consectetur adipiscing elit. Praesent nec erat ut nunc ultrices suscipit in in dui. Fusce adipiscing nisi eget ligula placerat hendrerit. Cras posuere sagittis tellus nec porta.</p>
    <p>Fusce libero magna, lacinia in blandit eu, posuere in augue. Phasellus interdum velit non eros commodo a viverra lectus tempor. Nunc vel magna quam, vitae dignissim mi. Mauris pellentesque sapien et nisl interdum elementum nec vitae mi. Lorem ipsum dolor sit amet, consectetur adipiscing elit.</p>
    <p class="more">Curabitur quis fringilla elit.</p>
  </div>
  <a class="btn-blue">Search Offers</a>

  <div class="domain-table offer-table">
    <div class="offer-head">Half price domains –&nbsp;<em>Only 15:36:14 left.</em></div>
    <div class="domain-row"><div class="domain-name">tradingmytablet.com</div><div class="domain-price">$1,000</div><div class="domain-go"><span class="go-btn"><svg width="20" height="18" viewBox="0 0 20 18"><path d="M2 2l7 7-7 7M10 2l7 7-7 7" fill="none" stroke="#fff" stroke-width="3"/></svg></span></div></div>
    <div class="domain-row"><div class="domain-name">notes-a.com</div><div class="domain-price">$750</div><div class="domain-go"><span class="go-btn"><svg width="20" height="18" viewBox="0 0 20 18"><path d="M2 2l7 7-7 7M10 2l7 7-7 7" fill="none" stroke="#fff" stroke-width="3"/></svg></span></div></div>
    <div class="domain-row"><div class="domain-name">vintage-vans.com</div><div class="domain-price">$450</div><div class="domain-go"><span class="go-btn"><svg width="20" height="18" viewBox="0 0 20 18"><path d="M2 2l7 7-7 7M10 2l7 7-7 7" fill="none" stroke="#fff" stroke-width="3"/></svg></span></div></div>
    <div class="domain-row"><div class="domain-name">shoe14.net</div><div class="domain-price">$400</div><div class="domain-go"><span class="go-btn"><svg width="20" height="18" viewBox="0 0 20 18"><path d="M2 2l7 7-7 7M10 2l7 7-7 7" fill="none" stroke="#fff" stroke-width="3"/></svg></span></div></div>
  </div>
</section>

<section class="browse">
  <h2 class="section-title">Browse <em>domains.</em></h2>
  <div class="domain-table browse-table">
    <div class="domain-row"><div class="domain-name">tradingmytablet.com</div><div class="domain-price">$1,000</div><div class="domain-go"><span class="go-btn"><svg width="20" height="18" viewBox="0 0 20 18"><path d="M2 2l7 7-7 7M10 2l7 7-7 7" fill="none" stroke="#fff" stroke-width="3"/></svg></span></div></div>
    <div class="domain-row"><div class="domain-name">notes-a.com</div><div class="domain-price">$750</div><div class="domain-go"><span class="go-btn"><svg width="20" height="18" viewBox="0 0 20 18"><path d="M2 2l7 7-7 7M10 2l7 7-7 7" fill="none" stroke="#fff" stroke-width="3"/></svg></span></div></div>
    <div class="domain-row"><div class="domain-name">vintage-vans.com</div><div class="domain-price">$450</div><div class="domain-go"><span class="go-btn"><svg width="20" height="18" viewBox="0 0 20 18"><path d="M2 2l7 7-7 7M10 2l7 7-7 7" fill="none" stroke="#fff" stroke-width="3"/></svg></span></div></div>
    <div class="domain-row"><div class="domain-name">shoe14.net</div><div class="domain-price">$400</div><div class="domain-go"><span class="go-btn"><svg width="20" height="18" viewBox="0 0 20 18"><path d="M2 2l7 7-7 7M10 2l7 7-7 7" fill="none" stroke="#fff" stroke-width="3"/></svg></span></div></div>
    <div class="domain-row"><div class="domain-name">tradingmytablet.com</div><div class="domain-price">$1,000</div><div class="domain-go"><span class="go-btn"><svg width="20" height="18" viewBox="0 0 20 18"><path d="M2 2l7 7-7 7M10 2l7 7-7 7" fill="none" stroke="#fff" stroke-width="3"/></svg></span></div></div>
    <div class="domain-row"><div class="domain-name">notes-a.com</div><div class="domain-price">$750</div><div class="domain-go"><span class="go-btn"><svg width="20" height="18" viewBox="0 0 20 18"><path d="M2 2l7 7-7 7M10 2l7 7-7 7" fill="none" stroke="#fff" stroke-width="3"/></svg></span></div></div>
    <div class="domain-row"><div class="domain-name">vintage-vans.com</div><div class="domain-price">$450</div><div class="domain-go"><span class="go-btn"><svg width="20" height="18" viewBox="0 0 20 18"><path d="M2 2l7 7-7 7M10 2l7 7-7 7" fill="none" stroke="#fff" stroke-width="3"/></svg></span></div></div>
    <div class="domain-row"><div class="domain-name">shoe14.net</div><div class="domain-price">$400</div><div class="domain-go"><span class="go-btn"><svg width="20" height="18" viewBox="0 0 20 18"><path d="M2 2l7 7-7 7M10 2l7 7-7 7" fill="none" stroke="#fff" stroke-width="3"/></svg></span></div></div>
    <div class="domain-row"><div class="domain-name">tradingmytablet.com</div><div class="domain-price">$1,000</div><div class="domain-go"><span class="go-btn"><svg width="20" height="18" viewBox="0 0 20 18"><path d="M2 2l7 7-7 7M10 2l7 7-7 7" fill="none" stroke="#fff" stroke-width="3"/></svg></span></div></div>
    <div class="domain-row"><div class="domain-name">notes-a.com</div><div class="domain-price">$750</div><div class="domain-go"><span class="go-btn"><svg width="20" height="18" viewBox="0 0 20 18"><path d="M2 2l7 7-7 7M10 2l7 7-7 7" fill="none" stroke="#fff" stroke-width="3"/></svg></span></div></div>
    <div class="domain-row"><div class="domain-name">vintage-vans.com</div><div class="domain-price">$450</div><div class="domain-go"><span class="go-btn"><svg width="20" height="18" viewBox="0 0 20 18"><path d="M2 2l7 7-7 7M10 2l7 7-7 7" fill="none" stroke="#fff" stroke-width="3"/></svg></span></div></div>
    <div class="domain-row"><div class="domain-name">shoe14.net</div><div class="domain-price">$400</div><div class="domain-go"><span class="go-btn"><svg width="20" height="18" viewBox="0 0 20 18"><path d="M2 2l7 7-7 7M10 2l7 7-7 7" fill="none" stroke="#fff" stroke-width="3"/></svg></span></div></div>
  </div>

  <nav class="pager">
    <span class="nav-btn prev">« Prev</span>
    <span class="pages"><span class="current">1</span><span>2</span><span>3</span><span>4</span><span>5</span></span>
    <span class="nav-btn">Next »</span>
  </nav>

  <aside class="adv">
    <h3 class="adv-title">Advanced <em>search</em></h3>
    <div class="adv-field">Keywords...</div>
    <div class="checks">
      <div class="check"><span class="box"><svg class="abs" style="left:-2px;top:-12px" width="44" height="44" viewBox="0 0 44 44"><path d="M4 22l12 14L40 6" fill="none" stroke="var(--green)" stroke-width="7"/></svg></span>All domains</div>
      <div class="check"><span class="box"></span>.com</div>
      <div class="check"><span class="box"></span>.net</div>
      <div class="check"><span class="box"></span>.org</div>
    </div>
    <div class="range">
      <div class="range-head"><span>Price range</span><em>$100 - 2,000</em></div>
      <div class="slider"><span class="fill" style="left:52px;width:184px"></span>
        <span class="knob" style="left:52px"><svg width="14" height="14" viewBox="0 0 14 14"><path d="M2 2l5 4 5-4M2 7l5 4 5-4" fill="none" stroke="#fff" stroke-width="2"/></svg></span>
        <span class="knob" style="left:220px"><svg width="14" height="14" viewBox="0 0 14 14"><path d="M2 7l5-4 5 4M2 12l5-4 5 4" fill="none" stroke="#fff" stroke-width="2"/></svg></span>
      </div>
    </div>
    <div class="range">
      <div class="range-head"><span>Length</span><em>5 - 10</em></div>
      <div class="slider"><span class="fill" style="left:20px;width:156px"></span>
        <span class="knob" style="left:20px"><svg width="14" height="14" viewBox="0 0 14 14"><path d="M2 2l5 4 5-4M2 7l5 4 5-4" fill="none" stroke="#fff" stroke-width="2"/></svg></span>
        <span class="knob" style="left:160px"><svg width="14" height="14" viewBox="0 0 14 14"><path d="M2 7l5-4 5 4M2 12l5-4 5 4" fill="none" stroke="#fff" stroke-width="2"/></svg></span>
      </div>
    </div>
    <a class="btn-blue">Filter results</a>
  </aside>
</section>

<section class="story" role="img" aria-label="Photo of a smiling carpenter in an apron in his workshop">
  <article class="story-card">
    <h2>Our success is all down to <em>your success.</em></h2>
    <div class="copy">
      <p>Lorem ipsum dolor sit amet, consectetur adipiscing elit. Praesent nec erat ut nunc ultrices suscipit in in dui. Fusce adipiscing nisi eget ligula placerat hendrerit. Cras posuere sagittis tellus nec porta.</p>
      <p>Fusce libero magna, lacinia in blandit eu, posuere in augue. Phasellus interdum velit non eros commodo a viverra lectus tempor. Nunc vel magna quam, vitae dignissim mi. Mauris pellentesque sapien et nisl interdum elementum nec vitae mi. Lorem ipsum dolor sit amet, consectetur adipiscing elit.</p>
    </div>
    <div class="who">Neil Harper Snr.</div>
    <div class="trade">Harper &amp; Harper Joinery</div>
    <div class="site">www.harpersjoinery.example</div>
  </article>
</section>

<footer class="site-footer">
  <span>© copyright 2013 ZEPRILO.com Ltd. All rights reserved.</span>
  <nav><span>Login</span>•<span>Register</span>•<span>ZEPRILO support</span>•<span>Terms &amp; conditions</span>•<span>Privacy policy</span></nav>
</footer>

</body>
</html>
```